Website Refresh of tvga-tl.com

INTRODUCTION: The Tolvane Valley Growth Alliance (TVGA) is a 501-C3 nonprofit regional economic development organization with the goals of creating jobs, strengthening, and supporting existing business, and increasing wealth and prosperity of the region. TVGA is a private/public consortium funded by the nine sectors of the region with membership from large employers, small businesses, utilities, educational institutions, non‐profits, city government, county government, financial institutions, and developers/real estate/contractors. Our region consists of Flagstaff, Winslow, Sedona and Camp Verde and all of Coconino County.

MISSION: “With our partners, we provide quality economic growth for Northern Arizona.”

PROJECT & DESCRIPTION: We are hoping to revitalize and strengthen our brand, creating a cohesive and impactful identity that resonates with our target audience. Utilization of recent strategic data should be incorporated to invoke personal, emotional, and genuine elements into promotional activities, ensuring that marketing strategies resonate on a human level rather than feeling impersonal or automated. Collaborating with our team to understand key messaging is imperative. Communicating who we are, what we do and why it’s important is key.
WEBSITE: Update the existing website for a comprehensive refresh. Our goal is to enhance the user experience, modernize the design and improve functionality to better align with our brand and goals outlined in the strategic plan.
The website should do the following:
• Engage website visitors with fresh and updated content.
• Capture website visitors and convert them into a lead.
• Refresh current website with more photo rich content.
• Create a page that shows available buildings or land options.
• Create a search function.
• Ensure mobile friendliness.
• Ensure that the website is user friendly.
Create a feature that allows us to upload properties in the region for sale or lease.

Please see the attached new logo which has yet to be launched as we want to roll it out with the website refresh. We are open to other features that you feel our website should have. Please also see our attached strategic roadmap.

```html
<!DOCTYPE html>
<html lang="en">
<head>
<meta charset="utf-8">
<title>TVGA – Tolvane Valley Growth Alliance</title>
<link href="https://fonts.googleapis.com/css2?family=Jost:wght@400;500;600&display=swap" rel="stylesheet">
<style>
:root{
  --blue:#2c6aa0;
  --blue-mid:#3a7fb5;
  --sky:#1f9ad6;
  --navy:#13233a;
  --ink:#1c2430;
  --text:#4a5563;
  --pale:#eef5fb;
  --line:#d7e2ec;
  --white:#fff;
}
*{box-sizing:border-box;margin:0;padding:0}
html,body{width:1200px;height:4640px;overflow:hidden}
body{font-family:"Jost",sans-serif;color:var(--ink);background:var(--white);position:relative}
.abs{position:absolute}
.eyebrow{font-size:11px;letter-spacing:2px;text-transform:uppercase;font-weight:500;color:var(--text)}
.h2{font-size:31px;font-weight:500;line-height:1.2;color:var(--ink)}
.accent{color:var(--sky)}
.body{font-size:11.5px;line-height:1.6;color:var(--text)}
.btn-outline{display:inline-block;border:1.5px solid var(--blue);color:var(--blue);font-size:11px;font-weight:500;padding:9px 24px;border-radius:2px}
.btn-solid{display:inline-block;background:var(--blue);color:var(--white);font-size:11px;font-weight:500;padding:9px 24px;border-radius:2px}
.photo{position:absolute}

/* nav */
.nav{top:0;left:0;width:1200px;height:61px;background:var(--blue);display:flex;align-items:center;padding:0 160px}
.nav .brand{color:var(--white);font-size:22px;font-weight:600;letter-spacing:.5px}
.nav ul{list-style:none;display:flex;gap:26px;margin-left:auto;margin-right:26px;color:var(--white);font-size:11px}
.nav ul li.active{border-bottom:2px solid var(--sky);padding-bottom:4px}
.nav .contact{background:var(--white);color:var(--blue);font-size:11px;font-weight:500;padding:9px 26px;border-radius:2px}

/* hero */
.hero{top:61px;left:0;width:1200px;height:476px;background:var(--pale)}
.hero h1{position:absolute;left:157px;top:130px;font-size:35px;font-weight:500;line-height:1.3;color:var(--ink)}
.hero .intro{position:absolute;left:157px;top:246px;width:390px;font-size:11.5px;line-height:1.6;color:var(--text)}
.search{position:absolute;left:157px;top:306px;width:375px;height:34px;background:var(--white);border:1px solid var(--line);font-size:11px;color:#9aa4ae;padding:10px 12px}
.search-btn{position:absolute;left:497px;top:306px;width:35px;height:34px;background:var(--blue);display:flex;align-items:center;justify-content:center}
.slider-arrows{position:absolute;left:518px;top:443px;display:flex;gap:4px}
.arrow{width:32px;height:32px;border:1px solid var(--blue);display:flex;align-items:center;justify-content:center;background:var(--white)}
.arrow.on{background:var(--blue)}

/* housing card */
.housing{top:497px;left:789px;width:252px;height:422px;background:var(--white);box-shadow:0 6px 24px rgba(20,40,70,.12);text-align:center;padding:20px 18px;z-index:3}
.housing h3{font-size:17px;font-weight:500;color:var(--blue);margin-bottom:18px}
.housing p{font-size:11px;line-height:1.6;color:var(--text);margin-bottom:14px}
.housing .cover{margin:22px auto 0;width:216px;height:188px;background:linear-gradient(135deg,#fcc23e,#f3a91f)}

/* about */
.about-text{top:690px;left:418px;width:320px}
.about-text h2{margin:16px 0 22px}
.about-text .body{margin-bottom:14px}

/* doing business */
.biz{top:1088px;left:0;width:600px;height:449px;background:var(--blue);color:var(--white);padding:65px 0 0 157px}
.biz .eyebrow{color:#dbe8f4}
.biz h2{color:var(--white);margin:14px 0 16px}
.biz .body{color:#e1ecf6;width:318px;margin-bottom:14px}
.biz .btn-outline{border-color:var(--white);color:var(--white);margin-top:6px}
.stats{top:1333px;left:533px;width:209px;height:288px;background:var(--pale);z-index:3;padding:22px 18px}
.stat{height:90px}
.stat b{display:block;font-size:24px;font-weight:500;color:var(--blue)}
.stat span{font-size:10.5px;color:var(--ink)}

/* living */
.living-text{top:1705px;left:645px;width:400px}
.living-text h2{margin:12px 0 14px}

/* services */
.services{top:1998px;left:0;width:1200px;height:389px;background:linear-gradient(180deg,#22354f,#1b2c44);text-align:center;padding-top:64px}
.services .eyebrow{color:#cfd9e4}
.services h2{color:var(--white);margin:14px auto 18px;width:520px}
.services .body{color:#cfd9e4;width:640px;margin:0 auto}
.card{top:2261px;width:284px;height:324px;color:var(--white);padding:28px 25px}
.card h4{font-size:16px;font-weight:500;margin:40px 0 14px;line-height:1.3;max-width:200px}
.card p{font-size:10.5px;line-height:1.65;color:#e4eef7;height:88px;overflow:hidden}
.card .more{font-size:10.5px;font-weight:500;margin-top:16px}

/* testimonials */
.testi-head{top:2652px;left:157px}
.testi-head h2{margin-top:18px}
.tab{top:2759px;left:333px;width:157px;height:33px;background:var(--sky);color:var(--white);font-size:10.5px;font-weight:600;letter-spacing:1.2px;display:flex;align-items:center;justify-content:center}
.quote{top:2842px;left:468px;width:560px}
.quote p{font-size:14px;line-height:1.6;color:var(--ink)}
.quote .name{font-size:18px;color:var(--blue);margin-top:30px}
.quote .role{font-size:11px;color:var(--ink);margin-top:4px}

/* news */
.news{top:3158px;left:0;width:1200px;height:603px;background:var(--pale);text-align:center}
.news .eyebrow{margin-top:70px}
.news h2{margin-top:20px}
.post{top:3331px;width:284px;height:302px;background:var(--white);border:1px solid var(--line)}
.post .img{height:187px}
.post .meta{font-size:10.5px;color:var(--blue);padding:14px 17px 8px}
.post h4{font-size:17px;font-weight:500;color:var(--blue);line-height:1.35;padding:0 17px;max-width:220px}
.viewall{top:3670px;left:546px}

/* cta */
.cta-bg{top:3761px;left:0;width:1200px;height:486px;background:linear-gradient(180deg,#f2f4f6,#d4d9de)}
.cta{top:3824px;left:157px;width:884px;height:337px;background:var(--blue);overflow:hidden}
.cta h2{position:absolute;left:50px;top:50px;width:420px;color:var(--white);font-size:30px;font-weight:500;line-height:1.2}
.cta p{position:absolute;left:50px;top:183px;width:420px;color:#e1ecf6;font-size:16px;line-height:1.6}
.cta .btn-solid{position:absolute;left:50px;top:260px;background:var(--white);color:var(--blue)}

/* footer */
.footer{top:4247px;left:0;width:1200px;height:343px;background:var(--navy)}
.contact-item{position:absolute;top:68px;display:flex;align-items:center;gap:14px;color:#dfe6ee;font-size:11px}
.icon-box{width:36px;height:36px;background:var(--sky);display:flex;align-items:center;justify-content:center}
.foot-brand{position:absolute;left:157px;top:176px;color:var(--white);font-size:24px;font-weight:600;display:flex;align-items:center;gap:8px}
.foot-brand i{display:block;width:12px;height:12px;background:var(--sky)}
.foot-about{position:absolute;left:157px;top:226px;width:420px;font-size:11px;line-height:1.6;color:#c9d3de}
.news-signup{position:absolute;left:681px;top:164px;width:360px}
.news-signup h4{font-size:17px;font-weight:400;color:var(--white);line-height:1.55}
.fields{display:flex;gap:12px;margin-top:16px}
.field{flex:1;border-bottom:1px solid #5a6b80;font-size:10px;color:#8fa0b3;padding-bottom:8px}
.signup-btn{display:inline-block;margin-top:22px;border:1.5px solid var(--white);color:var(--white);font-size:11px;padding:8px 22px}
.bottom{top:4590px;left:0;width:1200px;height:50px;background:var(--blue);color:#e1ecf6;font-size:10.5px;padding:0 157px;display:flex;align-items:center}
.socials{margin-left:auto;display:flex;gap:10px}
.socials span{width:24px;height:24px;background:#5b8fbd;display:block}
</style>
</head>
<body>

<header class="abs nav">
  <div class="brand">TVGA</div>
  <ul>
    <li class="active">Home</li><li>Doing Business Here</li><li>Living Here ▾</li><li>Resources &amp; Data</li><li>Talent &amp; Workforce</li><li>About TVGA ▾</li>
  </ul>
  <div class="contact">Contact Us</div>
</header>

<section class="abs hero">
  <svg class="abs" style="left:0;top:0" width="1200" height="476" role="img" aria-label="Red rock buttes under a clear blue sky">
    <defs><linearGradient id="rock" x1="0" y1="0" x2="0" y2="1"><stop offset="0" stop-color="#8fb7dc"/><stop offset=".45" stop-color="#b5714a"/><stop offset="1" stop-color="#6d4a34"/></linearGradient></defs>
    <polygon points="675,0 1200,0 1200,476 558,476" fill="url(#rock)"/>
  </svg>
  <h1><span class="accent">Inspiration</span> for Tomorrow’s<br>Opportunities</h1>
  <p class="intro">The Tolvane Valley Growth Alliance (TVGA) is a 501-C3 nonprofit regional economic development organization.</p>
  <div class="search">I would like to...</div>
  <div class="search-btn"><svg width="14" height="14" viewBox="0 0 14 14"><circle cx="6" cy="6" r="4.2" fill="none" stroke="#fff" stroke-width="1.5"/><line x1="9" y1="9" x2="12.5" y2="12.5" stroke="#fff" stroke-width="1.5"/></svg></div>
  <div class="slider-arrows">
    <div class="arrow"><svg width="12" height="10"><path d="M11 5H1M5 1L1 5l4 4" fill="none" stroke="#2c6aa0" stroke-width="1.3"/></svg></div>
    <div class="arrow on"><svg width="12" height="10"><path d="M1 5h10M7 1l4 4-4 4" fill="none" stroke="#fff" stroke-width="1.3"/></svg></div>
  </div>
</section>

<aside class="abs housing">
  <h3>Get Your Housing Report</h3>
  <p>Whether you’re a resident, business owner, or policymaker, understanding local housing conditions is key to making informed decisions.</p>
  <span class="btn-solid">Download Here</span>
  <div class="cover" role="img" aria-label="Housing report cover on a yellow background"></div>
</aside>

<div class="photo" style="top:650px;left:0;width:367px;height:438px;background:linear-gradient(180deg,#9fb3c6,#6f7f8e 45%,#4a4f52)" role="img" aria-label="Aerial view of a downtown skyline with mountains beyond"></div>
<section class="abs about-text">
  <div class="eyebrow">About us</div>
  <h2 class="h2">Empowering Northern<br><span class="accent">Arizona’s</span> Economy</h2>
  <p class="body">The Tolvane Valley Growth Alliance is your connector, facilitator and partner - whether you are a start-up just getting off the ground, an established business looking to expand, or a company wanting to relocate to the Northern Arizona region.</p>
  <p class="body">We serve as a central hub for collaboration—helping to attract new businesses, support existing employers, develop a skilled workforce, and improve the quality of life for everyone in the region.</p>
  <span class="btn-outline" style="margin-top:10px">Learn More</span>
</section>

<section class="abs biz">
  <div class="eyebrow">Grow, invest, succeed</div>
  <h2 class="h2">Doing Business Here</h2>
  <p class="body">The Tolvane Valley Growth Alliance is your connector, facilitator and partner - whether you are a start-up just getting off the ground, an established business looking to expand, or a company wanting to relocate to the Northern Arizona region.</p>
  <p class="body">We serve as a central hub for collaboration—helping to attract new businesses, support existing employers, develop a skilled workforce, and improve the quality of life for everyone in the region.</p>
  <span class="btn-outline">Learn More</span>
</section>
<div class="photo" style="top:1088px;left:600px;width:600px;height:449px;background:linear-gradient(180deg,#4c5560,#6b5a48 55%,#7a7a3e)" role="img" aria-label="Stone city welcome sign with wildflowers, video thumbnail"></div>
<svg class="abs" style="left:872px;top:1283px" width="56" height="56"><circle cx="28" cy="28" r="26" fill="none" stroke="#fff" stroke-width="2"/><path d="M23 18l14 10-14 10z" fill="#fff"/></svg>
<div class="abs stats">
  <div class="stat"><b>1,850</b><span>Job Opportunities Supported</span></div>
  <div class="stat"><b>$1.8 Billion</b><span>Annual Economic Contribution</span></div>
  <div class="stat"><b>43%</b><span>Cost-Burdened Households</span></div>
</div>

<div class="photo" style="top:1684px;left:157px;width:436px;height:251px;background:linear-gradient(180deg,#9c97b8,#c98a6a 45%,#7a4a36)" role="img" aria-label="Canyon landscape at sunset"></div>
<section class="abs living-text">
  <div class="eyebrow" style="color:var(--blue)">Built for life</div>
  <h2 class="h2">Living <span class="accent">Here</span></h2>
  <p class="body">What are your priorities? A beautiful, caring community in which to raise a family? An abundance of outdoor recreation? A vibrant arts community? Learn why cities in Northern Arizona top the charts for livability.</p>
  <span class="btn-outline" style="margin-top:16px">Learn More</span>
</section>

<section class="abs services">
  <div class="eyebrow">Our services</div>
  <h2 class="h2">Services that Connect Opportunity with Community</h2>
  <p class="body">By bringing new businesses to our region and strengthening those already here, our coalition of public, private and non-profit partners work to ensure the success of your business and the economic vitality of Northern Arizona.</p>
</section>
<article class="abs card" style="left:157px;background:var(--blue)">
  <svg width="56" height="56" viewBox="0 0 56 56" fill="none" stroke="#fff" stroke-width="1.6"><path d="M20 22a8 8 0 1 1 16 0"/><circle cx="14" cy="38" r="4"/><circle cx="28" cy="38" r="4"/><circle cx="42" cy="38" r="4"/><path d="M7 52a7 7 0 0 1 14 0M21 52a7 7 0 0 1 14 0M35 52a7 7 0 0 1 14 0"/></svg>
  <h4>Business Attraction</h4>
  <p>Creating more jobs is the key to increasing economic prosperity and vitality in the region. Since the founding of TVGA, the agency and its partners at the City of Tolvane, Greater Tolvane Partners...</p>
  <div class="more">Read More</div>
</article>
<article class="abs card" style="left:457px;background:var(--blue-mid)">
  <svg width="56" height="56" viewBox="0 0 56 56" fill="none" stroke="#fff" stroke-width="1.6"><circle cx="28" cy="16" r="9"/><path d="M24 16l3 3 5-6"/><circle cx="16" cy="36" r="4"/><circle cx="28" cy="34" r="4.5"/><circle cx="40" cy="36" r="4"/><path d="M8 52a8 8 0 0 1 16 0M19 52a9 9 0 0 1 18 0M32 52a8 8 0 0 1 16 0"/></svg>
  <h4>Workforce Development</h4>
  <p>Strategic workforce development, combined with efforts to bring more high-paying jobs to our region, is an important step in building the infrastructure we need to ensure continued growth and...</p>
  <div class="more">Read More</div>
</article>
<article class="abs card" style="left:757px;background:var(--sky)">
  <svg width="56" height="56" viewBox="0 0 56 56" fill="none" stroke="#fff" stroke-width="1.6"><circle cx="28" cy="26" r="7"/><path d="M8 14h14l6 4M48 38H34l-6-4M8 14v8M48 38v-8"/></svg>
  <h4>Business Retention &amp; Expansion</h4>
  <p>While northern Arizona is renown worldwide for its rural splendor, those of us who live, work and play here every day un...</p>
  <div class="more">Read More</div>
</article>

<section class="abs testi-head">
  <div class="eyebrow">Testimonials</div>
  <h2 class="h2">What <span class="accent">Our Partners</span> are Saying</h2>
</section>
<div class="abs" style="left:964px;top:2670px;display:flex;gap:11px">
  <div class="arrow"><svg width="12" height="10"><path d="M11 5H1M5 1L1 5l4 4" fill="none" stroke="#2c6aa0" stroke-width="1.3"/></svg></div>
  <div class="arrow on"><svg width="12" height="10"><path d="M1 5h10M7 1l4 4-4 4" fill="none" stroke="#fff" stroke-width="1.3"/></svg></div>
</div>
<svg class="abs" style="left:0;top:2750px" width="1200" height="320"><path d="M306 9H1200M306 9V60" stroke="#3a8fd0" stroke-width="1.2" fill="none"/><line x1="441" y1="313" x2="1200" y2="313" stroke="#3a8fd0" stroke-width="1.2"/></svg>
<div class="abs tab">SUCCESS STORIES</div>
<div class="photo" style="top:2815px;left:157px;width:284px;height:280px;background:linear-gradient(180deg,#cfd3d6,#8a9096 55%,#2a2e34)" role="img" aria-label="Portrait of the partner quoted"></div>
<blockquote class="abs quote">
  <p>At Brightpath Works, our mission is to remove barriers to opportunity and help individuals reach their full potential through the power of work. A strong local economy is essential to meeting that mission. Our collaboration with TVGA allows us to build the relationships and partnerships necessary for our northern Arizona communities to thrive.</p>
  <div class="name">Marco Velez</div>
  <div class="role">Brightpath Works of Central &amp; Northern Arizona, Director of Government Relations</div>
</blockquote>

<section class="abs news">
  <div class="eyebrow">Recent posts</div>
  <h2 class="h2">Latest News &amp; <span class="accent">Updates</span></h2>
</section>
<article class="abs post" style="left:157px">
  <div class="img" style="background:linear-gradient(180deg,#9cc0e0,#7b8e6a 60%,#5c6b4c)" role="img" aria-label="University campus with mountains behind"></div>
  <div class="meta">June 5, 2025</div><h4>The Power of A Thriving University</h4>
</article>
<article class="abs post" style="left:457px">
  <div class="img" style="background:linear-gradient(180deg,#f5f0e6,#e7a35c 60%,#2c6aa0)" role="img" aria-label="Economic development week promotional graphic with speaker portraits"></div>
  <div class="meta">May 16, 2025</div><h4>Celebrating Economic Development Week</h4>
</article>
<article class="abs post" style="left:757px">
  <div class="img" style="background:linear-gradient(135deg,#a7ae9c,#7d8a78)" role="img" aria-label="Aerial map of a development site"></div>
  <div class="meta">March 5, 2025</div><h4>Connecting with Site Selectors</h4>
</article>
<span class="abs btn-outline viewall">View All</span>

<div class="abs cta-bg" role="img" aria-label="Faded city skyline"></div>
<section class="abs cta">
  <svg class="abs" style="left:500px;top:0" width="384" height="337"><path d="M120 0H384V337H60C150 260 40 120 120 0Z" fill="#1f9ad6"/></svg>
  <div class="abs" style="left:640px;top:34px;width:195px;height:270px;background:linear-gradient(180deg,#d9c3a8,#f4f4f2);transform:rotate(14deg)" role="img" aria-label="Entrepreneurship guide brochure"></div>
  <h2>Interested in becoming an Entrepreneur in northern Arizona?</h2>
  <p>Discover the resources that are bringing startups to a higher elevation.</p>
  <span class="btn-solid">Get Your Guide</span>
</section>

<footer class="abs footer">
  <div class="contact-item" style="left:157px"><div class="icon-box"><svg width="14" height="16"><path d="M7 15s5-5 5-9A5 5 0 0 0 2 6c0 4 5 9 5 9z" fill="none" stroke="#fff" stroke-width="1.4"/><circle cx="7" cy="6" r="1.8" fill="#fff"/></svg></div>418 W. Cedar Ave., Suite 7 Tolvane, AZ 86099</div>
  <div class="contact-item" style="left:625px"><div class="icon-box"><svg width="16" height="16"><path d="M3 1l3 3-2 2c1 2 3 4 5 5l2-2 3 3-2 3C7 14 2 9 1 3z" fill="none" stroke="#fff" stroke-width="1.3"/></svg></div>(928) 555-0142</div>
  <div class="contact-item" style="left:919px"><div class="icon-box"><svg width="16" height="12"><rect x=".7" y=".7" width="14.6" height="10.6" fill="none" stroke="#fff" stroke-width="1.3"/><path d="M1 1l7 6 7-6" fill="none" stroke="#fff" stroke-width="1.3"/></svg></div>tvga-tl.com</div>
  <div class="foot-brand"><i></i>TVGA</div>
  <p class="foot-about">TVGA is an economic collaborative organization supported by a multitude of agencies in Northern Arizona. The agency coordinates the regional efforts of private, public, and nonprofit organizations that are working to improve economic vitality in northern Arizona.</p>
  <div class="news-signup">
    <h4>Keep up with the latest Economic Development news in northern Arizona!</h4>
    <div class="fields"><div class="field">First name</div><div class="field">Email</div></div>
    <span class="signup-btn">Sign Me Up</span>
  </div>
</footer>
<div class="abs bottom">
  Copyright © 2024 Tolvane Valley Growth Alliance. All Rights Reserved.
  <div class="socials"><span></span><span></span><span></span></div>
</div>

</body>
</html>
```